Business Card Design Project

We need a Business Card for an Mechanical Engineering firm in Singapore. The design should be Modern & Technical looking, yet eye catching.

Our company deals in Cutting Tools & Machine Accessories for the Manufacturing Industries such as Oil & Gas, Aero Space, etc... For more information on our Company, you can either email me or view our website www.torvale.com.sg.

We are trying to revamp our image to give our consumers a fresh new perspective to our company, so we welcome all ideas.

Industry/Entity Type

Business

Requirements
Must have
• Must incorporate New Company Logo into the card as shown in Uploaded file.

```html
<!DOCTYPE html>
<html lang="en">
<head>
<meta charset="utf-8">
<title>Torvale Tools – Business Card</title>
<link rel="stylesheet" href="https://fonts.googleapis.com/css2?family=Open+Sans:ital,wght@0,400;0,600;0,700;1,600;1,700&display=swap">
<style>
  :root {
    --stage: #0a090d;
    --brand-red: #8c1330;
    --deep-red: #5a0612;
    --mid-red: #9b1a2e;
    --text-grey: #555459;
    --card-white: #ffffff;
  }
  * { margin: 0; padding: 0; box-sizing: border-box; }
  html, body {
    width: 1200px; height: 1200px; overflow: hidden;
    background: var(--stage);
    font-family: "Open Sans", Arial, sans-serif;
  }
  .card {
    position: absolute; top: 443px;
    width: 521px; height: 313px;
    overflow: hidden;
  }
  .card--front {
    left: 54px;
    background: linear-gradient(100deg, var(--card-white) 45%, #ececed 100%);
  }
  .card--back {
    left: 624px;
    background: radial-gradient(ellipse at 45% 48%, #b8213d 0%, var(--mid-red) 30%, var(--deep-red) 75%, #3e030b 100%);
  }
  .gear-art {
    position: absolute; right: 0; bottom: 0;
    width: 260px; height: 220px;
    background: radial-gradient(circle at 70% 70%, #c9c9cb 0%, #dcdcde 45%, rgba(236,236,237,0) 75%);
  }
  .back-art {
    position: absolute; inset: 0;
    background: radial-gradient(circle at 25% 30%, rgba(60,2,10,.45) 0%, rgba(60,2,10,0) 35%),
                radial-gradient(circle at 80% 80%, rgba(60,2,10,.45) 0%, rgba(60,2,10,0) 35%);
  }
  .brand {
    position: absolute; left: 38px; top: 100px;
    display: flex; align-items: center; gap: 8px;
  }
  .brand__dot {
    width: 14px; height: 14px; border-radius: 50%;
    background: var(--brand-red);
  }
  .brand__name {
    font-size: 22px; font-weight: 700; letter-spacing: 1px;
    color: var(--brand-red);
  }
  .person {
    position: absolute; right: 40px; top: 32px; text-align: right;
  }
  .person__name {
    font-size: 24px; font-weight: 700; color: var(--brand-red); line-height: 1.1;
  }
  .person__role {
    font-size: 14px; font-weight: 600; font-style: italic; color: var(--text-grey);
    margin-top: 4px;
  }
  .address {
    position: absolute; left: 39px; top: 160px;
    font-size: 14px; line-height: 19px; color: var(--text-grey); font-style: normal;
  }
  .contacts {
    position: absolute; left: 40px; top: 208px;
    list-style: none; font-size: 14px; line-height: 19px; color: var(--text-grey);
  }
  .contacts li { display: flex; align-items: center; gap: 5px; }
  .contacts svg { width: 15px; height: 13px; flex: none; }
  .url-band {
    position: absolute; left: 0; right: 0; top: 144px; height: 27px;
    background: rgba(40, 0, 6, 0.55);
  }
  .url-band__text {
    position: absolute; right: 146px; top: -3px;
    font-size: 22px; font-weight: 700; font-style: italic; color: #ffffff;
  }
</style>
</head>
<body>
  <section class="card card--front">
    <div class="gear-art" role="img" aria-label="Soft grey gear illustration"></div>

    <div class="brand">
      <span class="brand__dot"></span>
      <span class="brand__name">TORVALE TOOLS</span>
    </div>

    <div class="person">
      <p class="person__name">John DOE</p>
      <p class="person__role">Director</p>
    </div>

    <address class="address">
      dummy&nbsp; dummy<br>
      dummy dummy City dummy
    </address>

    <ul class="contacts">
      <li>
        <svg viewBox="0 0 15 13"><path d="M1 4c2-3 11-3 13 0l-2 2-2-1V4H5v1L3 6z M3 7h9l1 5H2z" fill="var(--brand-red)"/></svg>
        (065) 481207
      </li>
      <li>
        <svg viewBox="0 0 15 13"><rect x="4" y="1" width="7" height="5" fill="none" stroke="var(--brand-red)"/><rect x="1.5" y="6" width="12" height="6" fill="none" stroke="var(--brand-red)"/></svg>
        (065) 4812079
      </li>
      <li>
        <svg viewBox="0 0 15 13"><rect x="5" y="1" width="5" height="11" rx="1" fill="none" stroke="var(--brand-red)"/><circle cx="7.5" cy="10" r=".8" fill="var(--brand-red)"/></svg>
        +65 918 4827301
      </li>
      <li>
        <svg viewBox="0 0 15 13"><rect x="1" y="2" width="13" height="9" fill="none" stroke="var(--brand-red)"/><path d="M1 2l6.5 5L14 2" fill="none" stroke="var(--brand-red)"/></svg>
        john@torvale.com.sg
      </li>
    </ul>
  </section>

  <section class="card card--back">
    <div class="back-art" role="img" aria-label="Dark red gear illustration"></div>
    <div class="url-band">
      <span class="url-band__text">www.torvale.com.sg</span>
    </div>
  </section>
</body>
</html>
```